Brovik Estate Services LLC. Commercial & Residential

PROFESSIONAL WINDOW WASHING! professional dryer vent cleaning (prevent fires, $aves money, Lowers your electric bill, save your dryer, less drying time, ask how!)gutter clean outs and tune-up *Lowest Price Quotes Guaranteed!Straightforward Consultancy and Advice to empower homeowners and find solutions that fit your budget!non pressure house cleaning "no pressure...No Damage!Interior & Exterior House Painting call for free in-home consultationPre & Post Tenant Clean-Up PaintGenerator Maintenance Comprehensive Landlord Services & REO (special requests considered) no job too small)!

I would like my business cards to be as professional as possible. I provide property services to commercial and residential clients and need these cards to draw attention and catch ones eye. I have never had business cards for this the services I provide. And I need them so that business owners will trust that our services are the best and also homeowners will call based on the information they see on these cards., I want the window washing service to be the main focal point because it the main service provided. thank you Added Saturday, July 4, 2015

Target Market(s)

Property Services and professional window cleaning highlighted on the front of card rounded edges for card and sleek eye catching cards thank you

Industry/Entity Type

Property Maintenance

Contact Information for Business Card

347-920-5516 Direct. brovikestateservicesllc@quelmora.com

Requirements
Must have
• Professional appearance and eye catch design Property Services as a general point with professional window washing as a highlighted service and all the rest of the services on back of card
Nice to have
• vivid colors but professional appearance

```html
<!DOCTYPE html>
<html lang="en">
<head>
<meta charset="utf-8">
<title>Brovik Estate Services LLC. – Business Card</title>
<link href="https://fonts.googleapis.com/css2?family=Didact+Gothic&family=Montserrat:wght@700;800&family=Tinos&display=swap" rel="stylesheet">
<style>
  :root {
    --page: #eef0f2;
    --card-white: #f7f7f7;
    --blue: #3a77b7;
    --blue-deep: #2f66a3;
    --blue-light: #4a88c6;
    --navy: #32496a;
    --charcoal: #2b2b2b;
    --ink: #3b3b3b;
    --white: #ffffff;
    --dot: #3a77b7;
  }
  * { box-sizing: border-box; margin: 0; padding: 0; }
  html, body { width: 1200px; height: 900px; overflow: hidden; }
  body {
    background: var(--page);
    position: relative;
    font-family: "Didact Gothic", sans-serif;
  }
  .card {
    position: absolute;
    left: 300px;
    width: 600px;
    height: 343px;
    border-radius: 14px;
    overflow: hidden;
    box-shadow: 0 6px 18px rgba(0,0,0,0.12);
  }
  .card--front { top: 86px; background: var(--card-white); }
  .card--back  { top: 471px; background: var(--blue); }
  .card__art { position: absolute; inset: 0; width: 100%; height: 100%; }

  /* Front */
  .brand { position: absolute; left: 40px; top: 34px; }
  .brand__name { font-size: 27px; color: var(--ink); letter-spacing: 0.3px; }
  .brand__tag { font-size: 17px; color: var(--ink); margin-top: 6px; }
  .brand__rule {
    margin-top: 10px; width: 300px;
    border-top: 2px dotted var(--dot);
  }
  .feature {
    position: absolute; left: 250px; top: 196px;
    color: var(--white); font-family: "Montserrat", sans-serif;
    line-height: 0.95;
  }
  .feature__small { font-size: 15px; font-weight: 700; letter-spacing: 0.6px; }
  .feature__big { font-size: 30px; font-weight: 800; }
  .contact {
    position: absolute; left: 24px; bottom: 20px;
    list-style: none; color: var(--white);
    font-family: "Tinos", serif; font-size: 17px; line-height: 1.5;
  }
  .contact li { display: flex; align-items: center; gap: 10px; }
  .contact svg { width: 16px; height: 16px; flex: none; }

  /* Back */
  .back-head { position: absolute; left: 32px; top: 22px; right: 32px; color: var(--white); }
  .back-head__name { font-size: 22px; }
  .back-head__rule { margin: 6px 0; border-top: 2px dotted rgba(255,255,255,0.8); width: 330px; }
  .back-head__tag { font-size: 14px; }
  .services {
    position: absolute; left: 32px; top: 102px; right: 30px;
    list-style: none; color: var(--white);
    font-family: "Tinos", serif; font-size: 12.5px; line-height: 1.25;
  }
  .services li { position: relative; padding-left: 16px; margin-bottom: 3px; }
  .services li::before {
    content: ""; position: absolute; left: 0; top: 4px;
    width: 7px; height: 7px; border: 1px solid var(--white);
  }
</style>
</head>
<body>

<section class="card card--front" aria-label="Business card front">
  <svg class="card__art" viewBox="0 0 600 343" aria-hidden="true">
    <polygon points="0,170 600,170 600,343 0,343" fill="var(--blue)"/>
    <polygon points="0,170 560,170 600,200 600,343 0,343" fill="var(--blue-light)" opacity="0.5"/>
    <polygon points="0,170 190,170 140,250 0,250" fill="var(--charcoal)"/>
    <polygon points="230,170 600,170 600,290 230,290" fill="var(--navy)"/>
    <polygon points="480,170 600,170 600,290 560,290" fill="var(--charcoal)" opacity="0.55"/>
  </svg>

  <div class="brand">
    <h1 class="brand__name">Brovik Estate Services LLC.</h1>
    <p class="brand__tag">Commercial &amp; Residential</p>
    <div class="brand__rule"></div>
  </div>

  <div class="feature">
    <div class="feature__small">PROFESSIONAL</div>
    <div class="feature__big">WINDOW WASHING!</div>
  </div>

  <ul class="contact">
    <li>
      <svg viewBox="0 0 16 16" aria-hidden="true"><path d="M4 1.5l2.5 3-1.5 2a9 9 0 0 0 4.5 4.5l2-1.5 3 2.5-1.5 2.5C7 14.5 1.5 9 1.5 3z" fill="var(--white)"/></svg>
      347-920-5516 Direct.
    </li>
    <li>
      <svg viewBox="0 0 16 16" aria-hidden="true"><rect x="1.5" y="3.5" width="13" height="9" fill="none" stroke="var(--white)"/><path d="M1.5 3.5l6.5 5 6.5-5M1.5 12.5l5-4.5M14.5 12.5l-5-4.5" fill="none" stroke="var(--white)"/></svg>
      brovikestateservicesllc@quelmora.com
    </li>
  </ul>
</section>

<section class="card card--back" aria-label="Business card back">
  <svg class="card__art" viewBox="0 0 600 343" aria-hidden="true">
    <rect width="600" height="343" fill="var(--blue)"/>
    <polygon points="0,0 600,0 600,60 0,200" fill="var(--blue-deep)"/>
    <polygon points="0,260 600,150 600,343 0,343" fill="var(--blue-deep)" opacity="0.6"/>
  </svg>

  <header class="back-head">
    <h2 class="back-head__name">Brovik Estate Services LLC.</h2>
    <div class="back-head__rule"></div>
    <p class="back-head__tag">Commercial &amp; Residential - SERVICES</p>
  </header>

  <ul class="services">
    <li>Professional Window Washing!</li>
    <li>Professional dryer vent cleaning (Prevent fires, Saves money, Lowers your electric bill, save your dryer, less drying time, ask how!)</li>
    <li>Gutter clean outs and tune-up *Lowest Price Quotes Guaranteed!</li>
    <li>Straightforward Consultancy and Advice to empower homeowners and find solutions that fit your budget!</li>
    <li>Non pressure house cleaning "no pressure...No Damage!</li>
    <li>Interior &amp; Exterior House Painting call for free in-home consultation</li>
    <li>Pre &amp; Post Tenant Clean-Up Paint</li>
    <li>Generator Maintenance Comprehensive Landlord Services &amp; REO (special requests considered) no job too small)!</li>
  </ul>
</section>

</body>
</html>
```